Etiketten-Design für Kaffee
Zielgruppe
Vertrieb von gerösteten hochwertigen regionalen Kaffee
Unsere Zielgruppe sollten schon alle sein da unser Ziel der Handel ist
Aufgabenstellung
Das Etikett kommt auf eine Membrandose d.h. einmal drum gewickelt geklebt Membrandose d 90 x 140 mm
Sammelt sich um ein Lebensmitteletikett d.h. Kaffee als ganze Bohne
Auf dem Verpackungsdeckel kommt ein latte art foto das ist schon von uns aus fertig , vlt könnte man sich an die Farben orientieren als Idee ( siehe Foto verp. latte art)
Besonderen Wert legen wir auf eine sehr sympathische Darstellung liebe zum Produkt und Nachhaltigkeit
Es handelt sich um ein regionales Produkt aus dem Raum Hannover
1 Grundlage für 3Etiketten (Produkte)
mirandosa
BIO Espresso (Etikett des Bio Espressos Sehr auffällig gestalten das es Bio Ist mit dem Siegel oder eine bestimmte Farbe)
Bohne
Espresso
Mokka
Gemahlen
slogan : AUS LIEBE ZUM KAFFEE Farben des Unternehmens Rot Weiß

```html
<!DOCTYPE html>
<html lang="de">
<head>
<meta charset="utf-8">
<title>mirandosa – Espresso Etikett</title>
<link rel="stylesheet" href="https://fonts.googleapis.com/css2?family=Oswald:wght@500&family=Quicksand:wght@500&display=swap">
<style>
  :root {
    --backdrop: #e4e4e4;
    --label-black: #2a2a2a;
    --brand-red: #d9443a;
    --brand-red-deep: #b8302a;
    --tone-light: #f7ecea;
    --tone-mid: #e9a39b;
    --tone-red: #d4493f;
    --ink-white: #f2f2f2;
  }
  html, body {
    margin: 0;
    width: 1200px;
    height: 900px;
    overflow: hidden;
    background: var(--backdrop);
  }
  .canvas {
    position: relative;
    width: 1200px;
    height: 900px;
  }
  .label {
    position: absolute;
    left: 0;
    top: 0;
  }
  .slogan-ring {
    font-family: "Oswald", "Arial Narrow", sans-serif;
    font-weight: 500;
    font-size: 31px;
    fill: var(--ink-white);
    letter-spacing: 1px;
  }
  .slogan-ring .dot { fill: var(--brand-red); }
  .brand-name {
    font-family: "Quicksand", "Helvetica", sans-serif;
    font-weight: 500;
    font-size: 56px;
    fill: #ffffff;
  }
  .brand-mark {
    fill: none;
    stroke: #ffffff;
    stroke-width: 8;
  }
</style>
</head>
<body>
<main class="canvas">
  <svg class="label" width="1200" height="900" viewBox="0 0 1200 900" xmlns="http://www.w3.org/2000/svg">
    <defs>
      <linearGradient id="band-red" x1="0" x2="1" y1="0" y2="0">
        <stop offset="0" stop-color="var(--brand-red-deep)"/>
        <stop offset="0.5" stop-color="var(--brand-red)"/>
        <stop offset="1" stop-color="var(--brand-red-deep)"/>
      </linearGradient>
      <radialGradient id="illustration-tones" cx="0.5" cy="0.45" r="0.75">
        <stop offset="0" stop-color="var(--tone-light)"/>
        <stop offset="0.6" stop-color="var(--tone-mid)"/>
        <stop offset="1" stop-color="var(--tone-red)"/>
      </radialGradient>
      <path id="ring-path" d="M410,565 V340 A190,190 0 0 1 790,340 V565"/>
    </defs>

    <rect class="label-top" x="320" y="90" width="560" height="480" fill="var(--label-black)"/>
    <rect class="label-band" x="320" y="570" width="560" height="240" fill="url(#band-red)"/>

    <path class="illustration-window" role="img"
          aria-label="Gravur-Illustration in Rot und Weiß: Widder im Anzug mit Fliege, eine Espressotasse haltend, vor einem Kaffeestrauch"
          d="M450,570 V340 A150,150 0 0 1 750,340 V570 Z" fill="url(#illustration-tones)"/>

    <text class="slogan-ring">
      <textPath href="#ring-path" textLength="1020" lengthAdjust="spacing" startOffset="8">AUS LIEBE ZUM KAFFEE <tspan class="dot">•</tspan> ESPRESSO <tspan class="dot">•</tspan> AUS LIEBE ZUM KAFFEE</textPath>
    </text>

    <circle class="brand-mark" cx="600" cy="668" r="36"/>
    <text class="brand-name" x="600" y="760" text-anchor="middle">mirandosa</text>
  </svg>
</main>
</body>
</html>
```